Verdalune Anti-Age Mask sticker design for brochure

We need a sticker go next or over our mother company logo and design info on the back of the brochure.
We develop, manufacture and market organic professional patch form skin solutions.

Feel free to explore and give us something we can use, for a near future change of look, that we are looking for, in order to work the US market
The Local company is :
Solvenra LLC
37 SW Ninth St. 4 Floor
Miami, FL 33158

Reason: Due to the few proposal i have decided to extend the submission deadline.. thank you...

Target Market(s)

estheticians , spa managers and workers, general public

Industry/Entity Type

It Company

Requirements
Must have
• Logo or similarity

```html
<!DOCTYPE html>
<html lang="en">
<head>
<meta charset="utf-8">
<title>Solvenra LLC Sticker</title>
<link rel="stylesheet" href="https://fonts.googleapis.com/css2?family=Montserrat:wght@400;600&display=swap">
<style>
  :root {
    --paper: #ffffff;
    --mist: #cfe3e2;
    --stone: #747066;
    --rim: #75736a;
    --label-text: #ffffff;
  }
  html, body {
    margin: 0;
    padding: 0;
    width: 1143px;
    height: 1200px;
    overflow: hidden;
    background: var(--paper);
  }
  .sticker {
    display: block;
    width: 1143px;
    height: 1200px;
  }
  .band-top { fill: var(--mist); }
  .band-bottom { fill: var(--stone); }
  .rim { fill: none; stroke: var(--rim); stroke-width: 6; }
  .brand-dot { fill: var(--mist); }
  .brand-name {
    font-family: "Montserrat", sans-serif;
    font-weight: 400;
    font-size: 70px;
    letter-spacing: 24px;
    fill: var(--stone);
  }
  .company-name {
    font-family: "Montserrat", sans-serif;
    font-weight: 600;
    font-size: 43px;
    fill: var(--label-text);
  }
  .company-address {
    font-family: "Montserrat", sans-serif;
    font-weight: 400;
    font-size: 38px;
    fill: var(--label-text);
  }
</style>
</head>
<body>
<svg class="sticker" viewBox="0 0 1143 1200" xmlns="http://www.w3.org/2000/svg">
  <defs>
    <clipPath id="sticker-face">
      <circle cx="577" cy="567" r="410"/>
    </clipPath>
  </defs>

  <g clip-path="url(#sticker-face)">
    <circle cx="577" cy="567" r="410" fill="var(--paper)"/>
    <rect class="band-top" x="150" y="150" width="860" height="237"/>
    <rect class="band-bottom" x="150" y="760" width="860" height="240"/>
  </g>
  <circle class="rim" cx="577" cy="567" r="410"/>

  <g class="brand">
    <circle class="brand-dot" cx="262" cy="570" r="40"/>
    <text class="brand-name" x="340" y="596">Solvenra</text>
  </g>

  <g class="company-label" text-anchor="middle">
    <text class="company-name" x="577" y="818">Solvenra LLC</text>
    <text class="company-address" x="577" y="871">37 SW Ninth St. 4 Floor</text>
    <text class="company-address" x="577" y="917">Miami, FL 33158</text>
  </g>
</svg>
</body>
</html>
```